TBNW site redesign

Please redesign a home page with content provided. PSD only - no coding
Can use any images from Vexelmarq.com

Please create a site design that more clearly illustrates the client's services and expertise. We are looking for a high-end design.

Any images used must be generic or of Dallas TX.

Fonts: Any
Colors: Match to logo
Look: Modern - Professional

Target Market(s)

medium-large business owners

Number of Pages Required

1 page

Font styles to use
Serif
Sans Serif

Requirements
Must have
• cohesive professional design
• high end look
• Match to logo

```html
<!DOCTYPE html>
<html lang="en">
<head>
<meta charset="utf-8">
<title>TBNW – Office and Warehouse Tenant Representation</title>
<link rel="stylesheet" href="https://fonts.googleapis.com/css2?family=Libre+Baskerville:wght@400;700&family=Lato:ital,wght@0,400;0,700;1,400&family=Raleway:wght@600;700&display=swap">
<style>
:root{
  --red:#d0222b;
  --red-soft:#dc5150;
  --navy:#252a36;
  --navy-deep:#1d212b;
  --ink:#222;
  --text:#555;
  --muted:#888;
  --light:#f0f0f0;
  --white:#fff;
  --steel:#9aa3ad;
}
*{margin:0;padding:0;box-sizing:border-box}
html,body{width:1200px;height:3249px;overflow:hidden}
body{position:relative;font-family:"Lato",sans-serif;color:var(--text);background:var(--white)}
.abs{position:absolute}
.serif{font-family:"Libre Baskerville",serif}
.center{text-align:center}
a{color:inherit;text-decoration:none}

/* header */
.hero{left:0;top:0;width:1200px;height:617px;background:linear-gradient(180deg,#56606c 0%,#8c96a1 35%,#c3c9cf 70%,#dfe2e5 100%)}
.topbar{left:0;top:0;width:1200px;height:88px;background:var(--red)}
.logo-plate{left:0;top:0;width:330px;height:134px;background:var(--red);clip-path:polygon(0 0,100% 0,100% 66%,92% 100%,0 100%)}
.logo{left:120px;top:26px;background:var(--white);color:var(--red);font-family:"Libre Baskerville",serif;font-weight:700;font-size:40px;padding:6px 18px;line-height:1}
.logo-sub{left:120px;top:88px;color:var(--white);font-family:"Libre Baskerville",serif;font-size:13px;letter-spacing:1px}
.phone{left:808px;top:26px;display:flex;align-items:center;gap:14px;color:var(--white);font-family:"Libre Baskerville",serif;font-size:19px}
.phone-box{width:36px;height:36px;background:var(--white);border-radius:3px;display:flex;align-items:center;justify-content:center}
.nav{left:336px;top:88px;width:864px;height:38px;background:var(--navy);display:flex;padding-left:28px}
.nav a{color:var(--white);font-size:12.5px;text-transform:uppercase;line-height:38px;padding:0 30px;border-right:1px solid #3c4250}
.nav a.active{background:#121419}
.hero-arrow{top:340px}
.hero-title{left:0;width:1200px;top:322px;color:var(--white);font-family:"Raleway",sans-serif;font-weight:700;font-size:24px}
.hero-sub{left:0;width:1200px;top:362px;color:var(--white);font-size:19px;line-height:29px}

/* section headings */
.h2{left:0;width:1200px;font-family:"Libre Baskerville",serif;font-weight:700;font-size:27px;color:var(--ink);text-transform:uppercase;text-align:center}
.h2 em{font-style:normal;color:var(--red)}
.rule{height:1px;background:#ccc}
.rule b{position:absolute;left:50%;top:-1px;width:44px;height:3px;margin-left:-22px;background:var(--steel)}

.btn{background:var(--red-soft);color:var(--white);font-size:12px;text-transform:uppercase;text-align:center;line-height:36px;border-radius:2px}
.btn.dark{background:var(--navy)}

/* about */
.about-lead{left:200px;width:800px;top:752px;font-size:14px;font-weight:700;color:var(--ink)}
.about-text{left:170px;width:860px;top:786px;font-size:11.5px;line-height:20px;color:var(--ink)}

/* why */
.why{left:0;top:964px;width:1200px;height:448px;background:linear-gradient(135deg,#f6f6f7,#eceef0 60%,#f7f7f8)}
.feature{width:220px;text-align:center}
.feature .ring{width:128px;height:128px;margin:0 auto;border-radius:50%;border:2px solid #d5d5d5;padding:6px;background:var(--white)}
.feature .disc{width:112px;height:112px;border-radius:50%;background:var(--navy);display:flex;align-items:center;justify-content:center}
.feature.hot .disc{background:var(--red-soft)}
.feature h3{margin-top:26px;font-size:14px;font-weight:400;color:var(--ink)}
.feature.hot h3{color:var(--red)}
.feature p{margin-top:6px;font-size:11.5px;line-height:17px}
.feature .more{margin-top:6px;font-size:10.5px;text-transform:uppercase;color:var(--ink)}
.feature.hot .more{color:var(--red)}

/* cta band */
.cta{left:0;top:1412px;width:1200px;height:228px;background:var(--red-soft)}
.cta p{position:absolute;left:0;width:1200px;top:44px;color:var(--white);font-size:25px;line-height:36px;text-align:center}
.cta .btn{position:absolute;left:524px;top:135px;width:152px}

/* team */
.team-text{left:128px;width:944px;top:1776px;font-size:12px;line-height:23px;text-align:center;color:var(--ink)}
.photo{border-radius:50%;border:4px solid var(--white);box-shadow:0 0 0 1px #ddd}
.photo.lead{border:6px solid var(--red)}
.pin-tip{left:440px;top:2061px;width:0;height:0;border-left:15px solid transparent;border-right:15px solid transparent;border-top:20px solid var(--red)}
.bio-logo{left:175px;top:2196px;width:200px;text-align:center}
.bio-logo .mark{display:inline-block;background:var(--red);color:var(--white);font-family:"Libre Baskerville",serif;font-weight:700;font-size:30px;padding:4px 18px}
.bio-logo .name{margin-top:8px;font-family:"Libre Baskerville",serif;font-size:12px;color:#444;letter-spacing:.5px}
.bio-divider{left:454px;top:2144px;width:2px;height:195px;background:var(--red)}
.social-ring{width:28px;height:28px;border:1.5px solid var(--red);border-radius:50%;background:var(--white)}
.bio-name{left:505px;top:2140px;font-family:"Libre Baskerville",serif;font-weight:700;font-size:18px;color:var(--ink)}
.bio-role{left:505px;top:2170px;font-style:italic;font-size:13px;color:var(--muted)}
.bio-text{left:505px;width:575px;top:2194px;font-size:13px;line-height:24px;text-align:justify;color:var(--ink)}

/* news */
.news{left:0;top:2393px;width:1200px;height:375px;background:var(--light)}
.h3{font-family:"Libre Baskerville",serif;font-weight:700;font-size:24px;color:var(--ink);text-transform:uppercase}
.h3 em{font-style:normal;color:var(--red)}
.pager{display:flex;gap:3px}
.pager span{width:20px;height:20px;border:1.5px solid #555;display:flex;align-items:center;justify-content:center}
.pager span:first-child{border-color:var(--red)}
.col-rule{height:1px;background:#ccc}
.article{width:450px;display:flex;gap:18px}
.date{width:44px;text-align:center;flex:none}
.date .d{background:var(--navy);color:var(--white);font-size:19px;line-height:28px}
.date .m{background:var(--red);color:var(--white);font-size:10px;line-height:16px;text-transform:uppercase}
.article h4{font-size:14px;font-weight:700;color:var(--ink)}
.article p{margin-top:6px;font-size:11.5px;line-height:18px;color:var(--ink)}
.vline{left:600px;top:2475px;width:1px;height:235px;background:#ccc}
.quote{left:622px;width:455px;top:2548px;font-style:italic;font-size:11.5px;line-height:22px;color:var(--ink);text-indent:22px}
.quote-by{left:622px;top:2690px;font-size:14px;color:var(--red)}

/* footer */
.footer{left:0;top:2768px;width:1200px;height:433px;background:var(--navy)}
.f-head{font-family:"Libre Baskerville",serif;font-weight:700;font-size:14px;color:var(--white);text-transform:uppercase}
.f-rule{height:1px;background:#4a5060;margin-top:10px}
.f-links{list-style:none;font-size:12px;color:#dfe1e5;line-height:26.5px;margin-top:8px}
.f-links li::before{content:"• ";color:#dfe1e5}
.f-contact{font-size:12.5px;color:#dfe1e5;line-height:21px}
.f-row{display:flex;align-items:center;gap:12px;margin-top:16px}
.map{left:559px;top:2866px;width:262px;height:151px;background:linear-gradient(135deg,#e8eaee,#d8dde3 50%,#eef0f2);border:1px solid #fff}
.map-pin{left:683px;top:2924px}
.f-logo{left:905px;top:2865px;width:160px;text-align:center}
.f-logo .mark{display:inline-block;background:var(--white);color:var(--navy);font-family:"Libre Baskerville",serif;font-weight:700;font-size:30px;padding:4px 18px}
.f-logo .name{margin-top:10px;font-family:"Libre Baskerville",serif;font-size:12px;color:var(--white)}
.f-sep{left:120px;top:3047px;width:960px;height:1px;background:#4a5060}
.notices{left:0;width:1200px;top:3080px;text-align:center;font-size:12.5px;line-height:30.5px;color:#e2e4e8}
.notices .u{text-decoration:underline}
.copy-bar{left:0;top:3201px;width:1200px;height:48px;background:var(--red)}
.copy{left:120px;top:17px;font-size:11px;color:var(--white)}
.socials{left:990px;top:12px;display:flex;gap:10px}
.socials span{width:24px;height:24px;border-radius:50%;background:#1f5fa8;border:1.5px solid var(--white)}
.socials span:nth-child(2){background:#c9302c}
.socials span:nth-child(3){background:#1a6fb0}
</style>
</head>
<body>

<!-- header and hero -->
<div class="abs hero" role="img" aria-label="Wide interior of an empty modern warehouse with steel roof trusses and a polished concrete floor"></div>
<div class="abs topbar"></div>
<div class="abs logo-plate"></div>
<div class="abs logo">TBNW</div>
<div class="abs logo-sub">Bramwell Commercial Realty Group</div>
<div class="abs phone">
  <span class="phone-box"><svg width="18" height="18" viewBox="0 0 24 24"><path fill="#d0222b" d="M6.6 10.8a15.1 15.1 0 0 0 6.6 6.6l2.2-2.2c.3-.3.7-.4 1-.2 1.1.4 2.3.6 3.6.6.6 0 1 .4 1 1V20c0 .6-.4 1-1 1A17 17 0 0 1 3 4c0-.6.4-1 1-1h3.5c.6 0 1 .4 1 1 0 1.3.2 2.5.6 3.6.1.3 0 .7-.2 1z"/></svg></span>
  <span>Call Today: 214-555-0142</span>
</div>
<nav class="abs nav">
  <a class="active" href="#">Home</a><a href="#">About TBNW</a><a href="#">Services</a><a href="#">Blog</a><a href="#">Market News</a><a href="#">Contact Us</a>
</nav>
<svg class="abs hero-arrow" style="left:88px" width="26" height="56" viewBox="0 0 26 56"><path d="M24 2 2 28l22 26" fill="none" stroke="#fff" stroke-width="2" opacity=".8"/></svg>
<svg class="abs hero-arrow" style="left:1086px" width="26" height="56" viewBox="0 0 26 56"><path d="M2 2l22 26L2 54" fill="none" stroke="#fff" stroke-width="2" opacity=".8"/></svg>
<h1 class="abs hero-title center">PROFESSIONAL OFFICE AND WAREHOUSE LEASING</h1>
<p class="abs hero-sub center">Fast-track your search with tenant reps that only serve you,<br>and specialize in the DFW area.</p>

<!-- about -->
<h2 class="abs h2" style="top:668px">About <em>TBNW</em></h2>
<div class="abs rule" style="left:490px;top:721px;width:220px"><b></b></div>
<p class="abs about-lead center">Ut enim ad minim veniam, quis nostrud exercitation ullamco laboris nisi ut aliquip ex ea commodo consequat.</p>
<p class="abs about-text center">Lorem ipsum dolor sit amet, consectetur adipiscing elit, sed do eiusmod tempor incididunt ut labore et dolore magna aliqua. Ut enim ad minim veniam, quis nostrud exercitation ullamco laboris nisi ut aliquip ex ea commodo consequat. Duis aute irure dolor in reprehenderit in voluptate velit esse cillum dolore eu fugiat nulla pariatur. Excepteur sint occaecat cupidatat non proident, sunt in culpa qui officia deserunt mollit anim id est laborum</p>
<a class="abs btn" style="left:544px;top:866px;width:112px">Read More</a>

<!-- why tenant representation -->
<div class="abs why"></div>
<h2 class="abs h2" style="top:1016px">Why Tenant <em>Representation?</em></h2>
<div class="abs rule" style="left:350px;top:1072px;width:500px"><b></b></div>

<div class="abs feature hot" style="left:109px;top:1116px">
  <div class="ring"><div class="disc"><svg width="44" height="44" viewBox="0 0 24 24" fill="#fff"><circle cx="6" cy="8" r="2.5"/><circle cx="18" cy="8" r="2.5"/><circle cx="12" cy="15" r="2.5"/><path d="M6 8l6 7 6-7" stroke="#fff" stroke-width="1.2" fill="none"/></svg></div></div>
  <h3>Relationships</h3>
  <p>Save time by trusting TBNW year after<br>year to find the right location for</p>
  <div class="more">Read More ▸</div>
</div>
<div class="abs feature" style="left:375px;top:1116px">
  <div class="ring"><div class="disc"><svg width="40" height="40" viewBox="0 0 24 24" fill="none" stroke="#fff" stroke-width="1.6"><rect x="5" y="11" width="14" height="10" rx="2"/><path d="M8 11V7a4 4 0 0 1 8 0v4"/></svg></div></div>
  <h3>Access To More</h3>
  <p>We have no agreement or personal<br>incentives for specific properties</p>
  <div class="more">Read More ▸</div>
</div>
<div class="abs feature" style="left:626px;top:1116px">
  <div class="ring"><div class="disc"><svg width="40" height="40" viewBox="0 0 24 24" fill="none" stroke="#fff" stroke-width="2"><path d="M5 12.5l4.5 4.5L19 7"/></svg></div></div>
  <h3>Free To You</h3>
  <p>You pay us nothing. We get our<br>commission from the property</p>
  <div class="more">Read More ▸</div>
</div>
<div class="abs feature" style="left:871px;top:1116px">
  <div class="ring"><div class="disc"><svg width="40" height="40" viewBox="0 0 24 24" fill="#fff"><path d="M12 3l2.6 5.4 5.9.8-4.3 4.1 1 5.8L12 16.3 6.8 19.1l1-5.8L3.5 9.2l5.9-.8z"/></svg></div></div>
  <h3>Customized Service</h3>
  <p>Aside from saving you the time of<br>repeating what your needs</p>
  <div class="more">Read More ▸</div>
</div>

<!-- call to action -->
<section class="abs cta">
  <p>If you need to find office or warehouse space in the Dallas Fort Worth<br>area, the team at <b>TBNW</b> has the experience you need.</p>
  <a class="btn dark">Space Calculator</a>
</section>

<!-- team -->
<h2 class="abs h2" style="top:1692px">Meet <em>The Team</em></h2>
<div class="abs rule" style="left:450px;top:1746px;width:300px"><b></b></div>
<p class="abs team-text">At TBNW we believe that you deserve the best professional advice and personal service with your commercial real estate negotiations. By choosing TBNW as your tenant reps in the Dallas/Fort Worth area, you will receive the assistance of accomplished and experienced commercial real estate brokers and salespeople who are licensed by the State Realty Licensing Board to practice in Texas since 1982.</p>
<div class="abs photo lead" style="left:382px;top:1916px;width:146px;height:146px;background:linear-gradient(160deg,#c9b7a4,#8a6f58 60%,#d77a32)" role="img" aria-label="Portrait of the founder in a work jacket"></div>
<div class="abs pin-tip"></div>
<div class="abs photo" style="left:563px;top:1935px;width:112px;height:112px;background:linear-gradient(160deg,#e7e2dc,#a8805e 60%,#dfe3ea)" role="img" aria-label="Portrait of a team member"></div>
<div class="abs photo" style="left:705px;top:1935px;width:112px;height:112px;background:linear-gradient(160deg,#d9d4cf,#5b3d2c 55%,#2c5aa8)" role="img" aria-label="Portrait of a team member"></div>

<div class="abs bio-logo"><span class="mark">TBNW</span><div class="name">Bramwell Commercial Realty Group</div></div>
<div class="abs bio-divider"></div>
<div class="abs social-ring" style="left:441px;top:2204px"></div>
<div class="abs social-ring" style="left:441px;top:2244px"></div>
<div class="abs bio-name">Martin R. Hollis</div>
<div class="abs bio-role">Founder and President</div>
<p class="abs bio-text">Lorem ipsum dolor sit amet, consectetuer adipiscing elit, sed diam nonummy nibh euismod tincidunt ut laoreet dolore magna aliquam erat volutpat. Ut wisi enim ad minim veniam, quis nostrud exerci tation ullamcorper mori suscipit lobortis nisl ut aliquip ex ea commodo consequat. Duis autem vel eum iriure dolor in hendrerit in vulpk utate velit esse molestie consequat, vel illum dolore eu feugiat nulla facilisis at vero eros et accumsan et iuston odio dignissim qui blandit praesent luptatum zzril delenit augue duis dolore te feugait nulla facilisi</p>

<!-- articles and testimonials -->
<div class="abs news"></div>
<h3 class="abs h3" style="left:120px;top:2450px">Recent <em>Articles</em></h3>
<div class="abs pager" style="left:528px;top:2454px"><span><svg width="8" height="10"><path d="M7 1 2 5l5 4" stroke="#d0222b" fill="none" stroke-width="1.5"/></svg></span><span><svg width="8" height="10"><path d="M1 1l5 4-5 4" stroke="#333" fill="none" stroke-width="1.5"/></svg></span></div>
<div class="abs col-rule" style="left:120px;top:2496px;width:455px"></div>
<div class="abs article" style="left:120px;top:2546px">
  <div class="date"><div class="d">08</div><div class="m">May</div></div>
  <div><h4>Diam Nonummy Nibh Euism Od Tincidunt</h4><p>Lorem ipsum dolor sit amet, consectetuer adipiscing elit, sedi dia nummy nibh euismod tincidunt ut laoreet doloremoi magna aliquam</p></div>
</div>
<div class="abs col-rule" style="left:120px;top:2630px;width:455px"></div>
<div class="abs article" style="left:120px;top:2646px">
  <div class="date"><div class="d">08</div><div class="m">May</div></div>
  <div><h4>Diam Nonummy Nibh Euism Od Tincidunt</h4><p>Lorem ipsum dolor sit amet, consectetuer adipiscing elit, sedi dia nummy nibh euismod tincidunt ut laoreet doloremoi magna aliquam</p></div>
</div>
<div class="abs vline"></div>
<h3 class="abs h3" style="left:622px;top:2450px">Client <em>Testimonials</em></h3>
<div class="abs pager" style="left:1030px;top:2454px"><span><svg width="8" height="10"><path d="M7 1 2 5l5 4" stroke="#d0222b" fill="none" stroke-width="1.5"/></svg></span><span><svg width="8" height="10"><path d="M1 1l5 4-5 4" stroke="#333" fill="none" stroke-width="1.5"/></svg></span></div>
<div class="abs col-rule" style="left:622px;top:2496px;width:455px"></div>
<svg class="abs" style="left:622px;top:2548px" width="16" height="12" viewBox="0 0 16 12" fill="#999"><path d="M0 12V6l4-6h2L4 6h3v6zm9 0V6l4-6h2l-2 6h3v6z"/></svg>
<p class="abs quote">The real estate team at TBNW has decades of experience in Commercial. One advantage of TBNW is they know all the properties that are about to become available, BEFORE they are available. They have the inside track on properties and they watch your back at the negotiating table. Very impressive with a polished approach. Let the team run with your next project and you won't be disappointed</p>
<div class="abs quote-by">~ Andrew Paul Whitford</div>

<!-- footer -->
<footer class="abs footer"></footer>
<div class="abs" style="left:120px;top:2822px;width:120px">
  <div class="f-head">Quick Links</div><div class="f-rule"></div>
  <ul class="f-links"><li>Home</li><li>About Tbnw</li><li>Services</li><li>Blog</li><li>Market News</li><li>Contact Us</li></ul>
</div>
<div class="abs" style="left:295px;top:2822px;width:230px">
  <div class="f-head">Contact Information</div><div class="f-rule"></div>
  <div class="f-contact" style="margin-top:14px">412 Cedar Crest Avenue, Suite 300,<br>Dallas, TX 75201</div>
  <div class="f-contact f-row"><svg width="12" height="12" viewBox="0 0 24 24"><path fill="#dfe1e5" d="M6.6 10.8a15.1 15.1 0 0 0 6.6 6.6l2.2-2.2c.3-.3.7-.4 1-.2 1.1.4 2.3.6 3.6.6.6 0 1 .4 1 1V20c0 .6-.4 1-1 1A17 17 0 0 1 3 4c0-.6.4-1 1-1h3.5c.6 0 1 .4 1 1 0 1.3.2 2.5.6 3.6.1.3 0 .7-.2 1z"/></svg>214-555-0142</div>
  <div class="f-contact f-row"><svg width="12" height="12" viewBox="0 0 24 24" fill="none" stroke="#dfe1e5" stroke-width="2"><rect x="4" y="3" width="16" height="18" rx="2"/><path d="M8 8h8M8 12h8"/></svg>214-555-0187</div>
  <div class="f-contact f-row"><svg width="12" height="10" viewBox="0 0 24 18" fill="none" stroke="#dfe1e5" stroke-width="2"><rect x="1" y="1" width="22" height="16"/><path d="M1 1l11 9 11-9"/></svg>info@tbnw.com</div>
</div>
<div class="abs" style="left:559px;top:2822px;width:262px">
  <div class="f-head">Location Map</div><div class="f-rule"></div>
</div>
<div class="abs map" role="img" aria-label="Street map of the Dallas office location"></div>
<svg class="abs map-pin" width="20" height="28" viewBox="0 0 20 28"><path d="M10 0a10 10 0 0 0-10 10c0 7 10 18 10 18s10-11 10-18A10 10 0 0 0 10 0z" fill="#d0222b"/><circle cx="10" cy="10" r="3.5" fill="#fff"/></svg>
<div class="abs f-logo"><span class="mark">TBNW</span><div class="name">Bramwell Commercial Realty Group</div></div>
<div class="abs f-sep"></div>
<div class="abs notices">
  <div>State Realty Licensing Board Mandated Disclosure Notices</div>
  <div class="u">State Realty Licensing Board Information About Brokerage Services</div>
  <div class="u">State Realty Licensing Board Consumer Protection Notice</div>
</div>
<div class="abs copy-bar">
  <div class="abs copy">Copyright © 2018 TBNW. All Right Reserved.</div>
  <div class="abs socials"><span></span><span></span><span></span></div>
</div>

</body>
</html>
```